Electrician Company Website Design

I am looking to get a website designed only. I do not need it converted ot html. I simply need the design in a psd format. I have my own team for the conversion. The website is for an electrician company called Brightwater electric. I have created a txt document with the project parameters and specifics. I have also uploaded their logo in all avaible formats. It's a zip file.

Number of Pages Required

1 page

```html
<!DOCTYPE html>
<html lang="en">
<head>
<meta charset="utf-8">
<title>Brightwater Electric</title>
<link rel="stylesheet" href="https://fonts.googleapis.com/css2?family=Oswald:wght@400;500&family=Montserrat:wght@400;500;600&display=swap">
<style>
:root{
  --ink:#2b2d33;
  --muted:#6c6e75;
  --steel:#7b7d86;
  --steel-dark:#6a6c74;
  --white:#ffffff;
  --paper:#f4f4f5;
  --red:#e3262c;
  --line:#d8d8dc;
}
*{box-sizing:border-box;margin:0;padding:0}
html,body{width:1200px;height:4556px;overflow:hidden}
body{position:relative;font-family:'Montserrat',sans-serif;color:var(--ink);background:var(--white)}
.abs{position:absolute}
.heading{font-family:'Oswald',sans-serif;font-weight:500;text-transform:uppercase;letter-spacing:.5px}

/* hero */
.hero{left:0;top:0;width:1200px;height:707px;background:linear-gradient(100deg,#3c3a2f 0%,#5a5440 35%,#7d7e80 60%,#4c5466 100%)}
.brand{font-family:'Montserrat',sans-serif;font-weight:600;font-size:26px;display:flex;align-items:center;gap:12px;white-space:nowrap}
.brand-dot{width:34px;height:34px;border-radius:50%;flex:none}
.hero-brand{left:92px;top:66px;color:var(--white)}
.hero-brand .brand-dot{background:var(--white)}
.callbar{right:112px;top:20px;color:var(--white);font-family:'Oswald',sans-serif;font-size:17px;display:flex;align-items:center;gap:10px;white-space:nowrap}
.callbar .ring{width:36px;height:36px;border:1.5px solid var(--white);border-radius:50%;display:flex;align-items:center;justify-content:center}
.nav{right:112px;top:80px;display:flex;gap:23px;font-family:'Oswald',sans-serif;font-size:17px;color:var(--white);text-transform:uppercase;white-space:nowrap}
.hero-title{left:110px;top:258px;font-size:60px;line-height:72px;color:var(--white);letter-spacing:0;white-space:nowrap}
.hero-sub{left:110px;top:346px;font-size:26px;color:var(--white);font-weight:500;white-space:nowrap}
.hero-cta{left:111px;top:415px;width:226px;height:66px;border:1.5px solid var(--white);color:var(--white);font-size:19px;font-weight:500;display:flex;align-items:center;justify-content:center;text-transform:uppercase}

/* welcome */
.welcome-photo{left:111px;top:783px;width:500px;height:482px;background:linear-gradient(135deg,#2a4a8a,#1d2e58 55%,#b8741c);border-top-right-radius:70px}
.welcome-card{left:611px;top:839px;width:477px;height:426px;background:var(--white);box-shadow:0 6px 28px rgba(0,0,0,.12);padding:0 45px}
.welcome-card h2{margin-top:40px;font-size:40px;line-height:46px}
.welcome-card p{margin-top:30px;font-size:16px;line-height:26.5px;color:var(--muted)}
.btn-dark{border:1.5px solid var(--ink);font-size:17px;font-weight:500;display:flex;align-items:center;justify-content:center;text-transform:uppercase;color:var(--ink)}
.welcome-card .btn-dark{margin-top:25px;width:160px;height:53px}

/* services */
.services{left:0;top:1348px;width:1200px;height:782px;background:var(--steel)}
.section-title{left:0;width:1200px;text-align:center;font-size:40px;line-height:50px}
.services-title{top:1416px;color:var(--white)}
.svc{width:240px;text-align:center;color:var(--white);font-size:22px;font-weight:500;line-height:28px}
.svc-ring{width:152px;height:152px;margin:0 auto 14px;border:2px solid var(--white);border-radius:50%;display:flex;align-items:center;justify-content:center}
.svc-ring.active{background:var(--white)}
.svc-detail-title{left:110px;top:1812px;font-size:26px;color:var(--white);font-weight:500}
.svc-detail-text{left:110px;top:1868px;width:475px;font-size:16px;line-height:25.5px;color:var(--white)}
.svc-photo{left:673px;top:1776px;width:415px;height:300px;background:linear-gradient(120deg,#f2f2f0,#d6d6d4 55%,#3b3b3e);border-top-left-radius:60px}

/* areas */
.area-map{left:110px;top:2170px;width:420px;height:473px;background:linear-gradient(160deg,#f7f7f7,#ececec);border:1.5px solid #c9c9c9}
.areas-title{left:595px;top:2250px;font-size:40px;line-height:50px}
.areas-text{left:595px;top:2323px;width:500px;font-size:16px;line-height:24px;color:var(--muted)}
.area{font-size:20px;font-weight:500;display:flex;align-items:center;gap:4px;white-space:nowrap}

/* gallery */
.gallery{left:0;top:2712px;width:1200px;height:479px;background:var(--paper)}
.gallery-title{top:2760px}
.tile{top:2861px;width:281px;height:269px;border-top-right-radius:50px}
.arrow{width:42px;height:42px;border-radius:50%;background:var(--white);box-shadow:0 2px 8px rgba(0,0,0,.2);display:flex;align-items:center;justify-content:center}

/* faq */
.faq-title{top:3252px}
.faq{left:221px;width:758px;height:50px;border:1px solid #e4e4e6;border-radius:4px;box-shadow:0 2px 6px rgba(0,0,0,.06);padding:0 32px;display:flex;align-items:center;justify-content:space-between;font-size:18px;font-weight:500;background:var(--white);white-space:nowrap}
.faq.open{background:var(--steel-dark);color:var(--white);border-color:var(--steel-dark)}
.faq-answer{left:254px;top:3428px;width:660px;font-size:16px;line-height:28px;color:var(--muted)}

/* contact */
.contact-info{left:0;top:3834px;width:413px;height:460px;background:var(--steel)}
.contact-form-bg{left:413px;top:3834px;width:787px;height:460px;background:linear-gradient(120deg,#1f2124,#3a3c40 50%,#25272a)}
.info-title{left:111px;top:3908px;font-size:22px;font-weight:600;color:var(--white)}
.info-row{left:111px;display:flex;align-items:center;gap:14px;color:var(--white);font-size:16px;line-height:28px;white-space:nowrap}
.info-ring{width:42px;height:42px;border:1.5px solid var(--white);border-radius:50%;display:flex;align-items:center;justify-content:center;flex:none}
.contact-title{left:456px;top:3890px;font-size:40px;line-height:50px;color:var(--white)}
.field{background:var(--white);border:1px solid var(--line);font-size:16px;color:#888;padding:10px 15px}
.send{left:452px;top:4167px;width:121px;height:51px;border:1.5px solid var(--white);border-radius:26px;color:var(--white);font-size:19px;font-weight:500;display:flex;align-items:center;justify-content:center;text-transform:uppercase}

/* footer */
.footer-brand{left:106px;top:4400px;font-size:30px;color:var(--ink)}
.footer-brand .brand-dot{background:var(--ink)}
.social{top:4355px;width:44px;height:44px;border:1.5px solid var(--ink);border-radius:50%}
.footer-links{left:486px;top:4418px;display:flex;gap:22px;font-size:16px;color:var(--muted);white-space:nowrap}
.copyright{left:486px;top:4456px;font-size:16px;color:var(--muted);white-space:nowrap}
</style>
</head>
<body>

<!-- hero -->
<section class="abs hero" role="img" aria-label="Photo of an electrician in a hard hat testing wiring with a multimeter"></section>
<div class="abs brand hero-brand"><span class="brand-dot"></span>Brightwater electric</div>
<div class="abs callbar"><span class="ring"><svg width="16" height="16" viewBox="0 0 24 24"><path fill="#fff" d="M6.6 10.8a15 15 0 0 0 6.6 6.6l2.2-2.2a1 1 0 0 1 1-.25 11.4 11.4 0 0 0 3.6.57 1 1 0 0 1 1 1V20a1 1 0 0 1-1 1A17 17 0 0 1 3 4a1 1 0 0 1 1-1h3.5a1 1 0 0 1 1 1c0 1.25.2 2.45.57 3.57a1 1 0 0 1-.25 1z"/></svg></span>CALL US NOW: 555 010 4472</div>
<nav class="abs nav"><span>Company</span><span>Services</span><span>Service Area</span><span>Gallery</span><span>FAQs</span><span>Contact</span></nav>
<h1 class="abs heading hero-title">Brightwater Electric</h1>
<p class="abs hero-sub">We are an electrician company</p>
<div class="abs hero-cta">Get More Info</div>

<!-- welcome -->
<div class="abs welcome-photo" role="img" aria-label="Photo of a smiling electrician on a ladder cutting wires"></div>
<div class="abs welcome-card">
  <h2 class="heading">Welcome to<br>Brightwater Electric</h2>
  <p>Lorem ipsum dolor sit amet, consectetur adipis cing elit, sed do eiusmod tempor incididunt ut labore et dolore magna aliqua. Ut enim ad inim veniam, quis nostrud exercitation ullamco labris nisi ut aliquip ex ea commodo consequat. Duis aute irure dolor in reprehen.</p>
  <div class="btn-dark">Read More</div>
</div>

<!-- services -->
<section class="abs services"></section>
<h2 class="abs heading section-title services-title">Our Services</h2>
<div class="abs svc" style="left:200px;top:1499px">
  <div class="svc-ring"><svg width="78" height="78" viewBox="0 0 78 78" fill="none" stroke="#fff" stroke-width="2"><rect x="10" y="30" width="22" height="40"/><rect x="32" y="12" width="20" height="58"/><rect x="52" y="36" width="18" height="34"/><path d="M15 38h4M23 38h4M15 46h4M23 46h4M15 54h4M23 54h4M37 20h4M43 20h4M37 30h4M43 30h4M37 40h4M43 40h4M37 50h4M43 50h4M57 44h8M57 52h8M57 60h8"/></svg></div>
  Commerical<br>Electrical Services
</div>
<div class="abs svc" style="left:479px;top:1499px">
  <div class="svc-ring active"><svg width="78" height="78" viewBox="0 0 78 78" fill="none" stroke="#6a6c74" stroke-width="2.5"><path d="M12 38 39 12l27 26M18 33v34h42V33"/><path d="M39 67V32M39 48l-10-8v-6M39 42l10-8v-6"/><circle cx="29" cy="32" r="2.5"/><circle cx="49" cy="26" r="2.5"/><circle cx="39" cy="30" r="2.5"/></svg></div>
  Residential<br>Electrical Services
</div>
<div class="abs svc" style="left:758px;top:1499px">
  <div class="svc-ring"><svg width="78" height="78" viewBox="0 0 78 78" fill="none" stroke="#fff" stroke-width="2"><path d="M10 68V30h10v16l14-10v10l14-10v10l14-10v32z"/><path d="M14 30V14h6v16M10 68h60"/><path d="M20 58h6M32 58h6M44 58h6M56 58h6"/></svg></div>
  Industrial<br>Electrical Services
</div>
<h3 class="abs svc-detail-title">Residential Electrical Services</h3>
<p class="abs svc-detail-text">Lorem ipsum dolor sit amet, consectetur adipiscing elit, sed do eiusmod tempor incididunt ut labore et dolore magna aliqua. Ut enim ad minim veniam, quis nostrud exercitation ullamco laboris nisi ut aliquip ex ea commod o consequat. Duis aute irure dolor in reprehenderit in voluptate velit esse cillum dolore eu.</p>
<div class="abs svc-photo" role="img" aria-label="Photo of a technician servicing a wall-mounted air conditioner"></div>

<!-- service areas -->
<div class="abs area-map" role="img" aria-label="County map of Minnesota with pins marking the service area"></div>
<h2 class="abs heading areas-title">Service Areas</h2>
<p class="abs areas-text">Duis aute irure dolor in reprehenderit in voluptate velit esse cillum dolore eu fugiat nulla pariatur.</p>
<div class="abs area" style="left:595px;top:2413px"><svg width="12" height="17" viewBox="0 0 12 17"><path fill="#e3262c" d="M6 0a6 6 0 0 0-6 6c0 4.5 6 11 6 11s6-6.5 6-11a6 6 0 0 0-6-6zm0 8.5A2.5 2.5 0 1 1 6 3.5a2.5 2.5 0 0 1 0 5z"/></svg>Chisago MN</div>
<div class="abs area" style="left:595px;top:2457px"><svg width="12" height="17" viewBox="0 0 12 17"><path fill="#e3262c" d="M6 0a6 6 0 0 0-6 6c0 4.5 6 11 6 11s6-6.5 6-11a6 6 0 0 0-6-6zm0 8.5A2.5 2.5 0 1 1 6 3.5a2.5 2.5 0 0 1 0 5z"/></svg>Pine MN</div>
<div class="abs area" style="left:595px;top:2501px"><svg width="12" height="17" viewBox="0 0 12 17"><path fill="#e3262c" d="M6 0a6 6 0 0 0-6 6c0 4.5 6 11 6 11s6-6.5 6-11a6 6 0 0 0-6-6zm0 8.5A2.5 2.5 0 1 1 6 3.5a2.5 2.5 0 0 1 0 5z"/></svg>Carlton MN</div>
<div class="abs area" style="left:595px;top:2546px"><svg width="12" height="17" viewBox="0 0 12 17"><path fill="#e3262c" d="M6 0a6 6 0 0 0-6 6c0 4.5 6 11 6 11s6-6.5 6-11a6 6 0 0 0-6-6zm0 8.5A2.5 2.5 0 1 1 6 3.5a2.5 2.5 0 0 1 0 5z"/></svg>Washington MN</div>
<div class="abs area" style="left:827px;top:2413px"><svg width="12" height="17" viewBox="0 0 12 17"><path fill="#e3262c" d="M6 0a6 6 0 0 0-6 6c0 4.5 6 11 6 11s6-6.5 6-11a6 6 0 0 0-6-6zm0 8.5A2.5 2.5 0 1 1 6 3.5a2.5 2.5 0 0 1 0 5z"/></svg>Isanti MN</div>
<div class="abs area" style="left:827px;top:2457px"><svg width="12" height="17" viewBox="0 0 12 17"><path fill="#e3262c" d="M6 0a6 6 0 0 0-6 6c0 4.5 6 11 6 11s6-6.5 6-11a6 6 0 0 0-6-6zm0 8.5A2.5 2.5 0 1 1 6 3.5a2.5 2.5 0 0 1 0 5z"/></svg>Anoka MN</div>
<div class="abs area" style="left:827px;top:2501px"><svg width="12" height="17" viewBox="0 0 12 17"><path fill="#e3262c" d="M6 0a6 6 0 0 0-6 6c0 4.5 6 11 6 11s6-6.5 6-11a6 6 0 0 0-6-6zm0 8.5A2.5 2.5 0 1 1 6 3.5a2.5 2.5 0 0 1 0 5z"/></svg>Dakota MN</div>
<div class="abs area" style="left:827px;top:2546px"><svg width="12" height="17" viewBox="0 0 12 17"><path fill="#e3262c" d="M6 0a6 6 0 0 0-6 6c0 4.5 6 11 6 11s6-6.5 6-11a6 6 0 0 0-6-6zm0 8.5A2.5 2.5 0 1 1 6 3.5a2.5 2.5 0 0 1 0 5z"/></svg>Sherburne MN</div>

<!-- gallery -->
<section class="abs gallery"></section>
<h2 class="abs heading section-title gallery-title">Gallery</h2>
<div class="abs tile" style="left:14px;background:linear-gradient(135deg,#c8c4b8,#6d7080 60%,#e0a020)" role="img" aria-label="Photo of an electrician testing a fuse panel"></div>
<div class="abs tile" style="left:311px;background:linear-gradient(180deg,#5d88c4,#a9bfd8 40%,#e8d7b0 70%,#6a5a40)" role="img" aria-label="Photo of a modern house lit at dusk"></div>
<div class="abs tile" style="left:608px;background:linear-gradient(180deg,#2a8bd8,#5aa6dc 35%,#8a9aa8 70%,#2d3848)" role="img" aria-label="Photo of an industrial refinery plant"></div>
<div class="abs tile" style="left:905px;background:linear-gradient(135deg,#0d2448,#2a4a7a 45%,#c9a048 75%,#1a2a40)" role="img" aria-label="Photo of a glass office tower lit at night"></div>
<div class="abs arrow" style="left:0;top:2972px"><svg width="12" height="18" viewBox="0 0 12 18"><path d="M9 2 2 9l7 7" fill="none" stroke="#333" stroke-width="2"/></svg></div>
<div class="abs arrow" style="left:1156px;top:2972px"><svg width="12" height="18" viewBox="0 0 12 18"><path d="m3 2 7 7-7 7" fill="none" stroke="#333" stroke-width="2"/></svg></div>

<!-- faq -->
<h2 class="abs heading section-title faq-title">Frequently Asked Questions</h2>
<div class="abs faq open" style="top:3345px">What is Lorem ipsum dolor sit amet, consectetur adipiscing elit?<svg width="16" height="10" viewBox="0 0 16 10"><path d="m2 8 6-6 6 6" fill="none" stroke="#fff" stroke-width="2"/></svg></div>
<p class="abs faq-answer">Neque porro quisquam est, qui dolorem ipsum quia dolor sit amet, consectur, adipisci velit, sed quia non numquam eius modi tempora incidunt ut labore et dolore magnam aliquam quaerat voluptatem.</p>
<div class="abs faq" style="top:3520px">What is Lorem ipsum dolor sit amet, consectetur adipiscing elit?<svg width="16" height="10" viewBox="0 0 16 10"><path d="m2 2 6 6 6-6" fill="none" stroke="#333" stroke-width="2"/></svg></div>
<div class="abs faq" style="top:3584px">What is Lorem ipsum dolor sit amet, consectetur adipiscing elit?<svg width="16" height="10" viewBox="0 0 16 10"><path d="m2 2 6 6 6-6" fill="none" stroke="#333" stroke-width="2"/></svg></div>
<div class="abs faq" style="top:3648px">What is Lorem ipsum dolor sit amet, consectetur adipiscing elit?<svg width="16" height="10" viewBox="0 0 16 10"><path d="m2 2 6 6 6-6" fill="none" stroke="#333" stroke-width="2"/></svg></div>
<div class="abs faq" style="top:3714px">What is Lorem ipsum dolor sit amet, consectetur adipiscing elit?<svg width="16" height="10" viewBox="0 0 16 10"><path d="m2 2 6 6 6-6" fill="none" stroke="#333" stroke-width="2"/></svg></div>

<!-- contact -->
<section class="abs contact-info"></section>
<section class="abs contact-form-bg" role="img" aria-label="Photo of a wired electrical control cabinet"></section>
<h3 class="abs info-title">Contact Information</h3>
<div class="abs info-row" style="top:3975px"><span class="info-ring"><svg width="14" height="20" viewBox="0 0 12 17"><path fill="#fff" d="M6 0a6 6 0 0 0-6 6c0 4.5 6 11 6 11s6-6.5 6-11a6 6 0 0 0-6-6zm0 8.5A2.5 2.5 0 1 1 6 3.5a2.5 2.5 0 0 1 0 5z"/></svg></span><span>1420 Maple Run NE<br>Cedar Falls, MN 55090</span></div>
<div class="abs info-row" style="top:4048px"><span class="info-ring"><svg width="16" height="16" viewBox="0 0 24 24"><path fill="#fff" d="M6.6 10.8a15 15 0 0 0 6.6 6.6l2.2-2.2a1 1 0 0 1 1-.25 11.4 11.4 0 0 0 3.6.57 1 1 0 0 1 1 1V20a1 1 0 0 1-1 1A17 17 0 0 1 3 4a1 1 0 0 1 1-1h3.5a1 1 0 0 1 1 1c0 1.25.2 2.45.57 3.57a1 1 0 0 1-.25 1z"/></svg></span>555 010 4472</div>
<div class="abs info-row" style="top:4108px"><span class="info-ring"><svg width="18" height="14" viewBox="0 0 18 14"><rect x="1" y="1" width="16" height="12" rx="1" fill="#fff"/><path d="m1 2 8 6 8-6" fill="none" stroke="#7b7d86" stroke-width="1.5"/></svg></span>Email Us</div>
<h2 class="abs heading contact-title">Contact Us</h2>
<div class="abs field" style="left:456px;top:3979px;width:334px;height:45px">Name</div>
<div class="abs field" style="left:456px;top:4036px;width:334px;height:44px">Email*</div>
<div class="abs field" style="left:456px;top:4092px;width:334px;height:45px">Phone</div>
<div class="abs field" style="left:800px;top:3979px;width:324px;height:158px">Message</div>
<div class="abs send">Send</div>

<!-- footer -->
<div class="abs brand footer-brand"><span class="brand-dot"></span>Brightwater electric</div>
<span class="abs social" style="left:483px" aria-label="Social profile"></span>
<span class="abs social" style="left:535px" aria-label="Social profile"></span>
<span class="abs social" style="left:586px" aria-label="Social profile"></span>
<nav class="abs footer-links"><span>Company</span><span>Services</span><span>Service Area</span><span>Gallery</span><span>FAQs</span><span>Contact</span></nav>
<p class="abs copyright">Copyright © 2022, Brightwater electric. All rights reserved.</p>

</body>
</html>
```